verdant terraces simple classy business card design

my name is owen harlow and I run a gardening business aimed at high class verdant terraces. the business name is verdant terraces and our logo was designed on pixel forum .My clientel are anything from residential homes to businesses. I take pride in my work and know that I offer a service like no other in my area.
The business card will be used to represent my business and I want it to be not only rememberable, but simplistic and modern. Eye catching too. Of course I would like it relatable to gardening and appealing to the correct clientel - those being garden enthusiasts, prestigious homes and businesses that are after top of the line gardening services like no other on the market.
I am not a typical lawn mowing business so I don't want a typical card design that represents that. The gardens I work with are generally million dollar properties with owners who are very garden proud looking for upkeep and guidance from me along with sometimes whole new garden designs. I want the business cards to show to my clients that I take pride, as they do, in their garden. And I want them to know from my card that I am a professional, qualified horticulturist offering them a top of the line service for life. I want them to refer my business on. I want them to look at my business card and see class and professionalism in a modern unique bold way.
The card should be simple with the possibility of the logo on the front being embossed/debossed and my details on the back the card should have a organic garden feel it's very important to me that it is absolutely perfect
I am also very open to ideas and suggestions so look forward to seeing the designs. the business logo has been supplied with this project and I want the card to be double sided

Contact info is
Owen Harlow - Managing Director / Horticulturist
Phone : 0481 526 704
Email: owenharlow@verdantterraces.com.au

Target Market(s)

high class gardens residential and commercial

Industry/Entity Type

Gardener

Contact Information for Business Card

Contact info is
Phone : 0481 526 704

PLEASE MAKE CARD DOUBLE SIDED

Requirements
Must have
• organic simple classy modern feel
• must flow with the current logo that has been supplied with this project
• Double sided
• Must explain in a simple way that I deal with high end gardens and I'm a qualified horticulturist
Nice to have
• embossed debossed logo
Should not have
• shouldn't be to busy or cheap looking

```html
<!DOCTYPE html>
<html lang="en">
<head>
<meta charset="utf-8">
<title>Verdant Terraces — Business Card</title>
<link href="https://fonts.googleapis.com/css2?family=Roboto:wght@400;500&display=swap" rel="stylesheet">
<style>
  :root {
    --backdrop: #6e6e6e;
    --card-dark: #1d1d1d;
    --card-light: #f7f7f5;
    --silver: #c9c9c9;
    --leaf: #5c9e4e;
    --leaf-mid: rgba(92, 158, 78, 0.78);
    --leaf-soft: rgba(160, 205, 148, 0.45);
    --leaf-fade: rgba(247, 247, 245, 0);
    --ink: #3a3a3a;
    --ink-muted: #6c6c6c;
    --rule: #9a9a9a;
  }
  * { box-sizing: border-box; margin: 0; padding: 0; }
  html, body {
    width: 900px; height: 1200px; overflow: hidden;
    background: var(--backdrop);
    font-family: "Roboto", Arial, sans-serif;
  }
  .canvas { position: relative; width: 900px; height: 1200px; }
  .card {
    position: absolute; left: 170px; width: 560px; height: 320px;
    box-shadow: 0 14px 30px rgba(0,0,0,.35);
    overflow: hidden;
  }
  .card--front { top: 200px; background: var(--card-dark); }
  .card--back  { top: 640px; background: var(--card-light); }

  .brand {
    position: absolute; left: 0; right: 0; top: 50%;
    transform: translateY(-50%);
    display: flex; align-items: center; justify-content: center; gap: 14px;
  }
  .brand__dot { width: 26px; height: 26px; border-radius: 50%; background: var(--leaf); }
  .brand__name {
    color: var(--silver); font-size: 30px; font-weight: 400;
    letter-spacing: 4px; text-transform: uppercase;
  }

  .card__art {
    position: absolute; top: 0; right: 0; bottom: 0; width: 270px;
    background: radial-gradient(ellipse 75% 62% at 68% 52%,
      var(--leaf) 0%, var(--leaf-mid) 38%, var(--leaf-soft) 68%, var(--leaf-fade) 100%);
  }

  .contact { position: absolute; left: 56px; top: 108px; width: 252px; z-index: 1; }
  .contact__name { font-size: 25px; font-weight: 500; color: var(--ink); }
  .contact__role { font-size: 13px; color: var(--ink-muted); margin-top: 4px; }
  .contact__rule { height: 1px; background: var(--rule); margin: 12px 0; }
  .contact__line {
    display: flex; align-items: center; gap: 10px;
    font-size: 13.5px; color: var(--ink); margin-bottom: 8px; white-space: nowrap;
  }
  .contact__line svg { width: 14px; height: 14px; flex: none; }
</style>
</head>
<body>
<main class="canvas">
  <section class="card card--front" aria-label="Card front">
    <div class="brand">
      <span class="brand__dot"></span>
      <span class="brand__name">Verdant Terraces</span>
    </div>
  </section>

  <section class="card card--back" aria-label="Card back">
    <div class="card__art" role="img" aria-label="Large green leafy brand emblem decoration"></div>
    <div class="contact">
      <h1 class="contact__name">Owen Harlow</h1>
      <p class="contact__role">Managing Director / Horticulturist</p>
      <div class="contact__rule"></div>
      <p class="contact__line">
        <svg viewBox="0 0 24 24" aria-hidden="true"><path fill="#3a3a3a" d="M6.6 10.8a15.1 15.1 0 0 0 6.6 6.6l2.2-2.2a1 1 0 0 1 1-.25 11.4 11.4 0 0 0 3.6.57 1 1 0 0 1 1 1V20a1 1 0 0 1-1 1A17 17 0 0 1 3 4a1 1 0 0 1 1-1h3.5a1 1 0 0 1 1 1c0 1.25.2 2.45.57 3.6a1 1 0 0 1-.25 1z"/></svg>
        0481 526 704
      </p>
      <p class="contact__line">
        <svg viewBox="0 0 24 24" aria-hidden="true"><rect x="2" y="5" width="20" height="14" rx="1.5" fill="none" stroke="#3a3a3a" stroke-width="2"/><path d="M3 6l9 7 9-7" fill="none" stroke="#3a3a3a" stroke-width="2"/></svg>
        owenharlow@verdantterraces.com.au
      </p>
    </div>
  </section>
</main>
</body>
</html>
```